Hosted PBX VoIP Web Site Redesign WordPress Template

We offer hosted 'in the cloud' telephone services. Our current site is http://www.brimwoodvoicelink.com and the site needs a major work-over. The site MUST BE be completed in WordPress as a template design.
I want this new site to have a warm look and feel giving the impression that we give the best customer service for small to medium businesses. The target business customer is small business with 5 to 50 employees with remote working employees who need to stay in communications with other staff.
Differentiation from our competitors is what we are looking for. We have been selling hosted pbx services for more than 7 years, we own our data center and have been in the data center business since 2000. Here are some examples of what I would like to have as a new web site:
Other hosted PBX companies:
http://www.quorvelo.com/
http://www.mendrix.com/
http://www.telbrandor.com/
http://www.glimber.com/
http://www.swiftlinecall.com/
Not Hosted PBX companies, but sites I like are:
http://www.kelvarnet.com/
http://www.zorquill.com/
http://www.plintbox.com/
I don't want a copy-cat web site and will invest in good graphics and original photography and graphics as needed.
Dana Worley
http://www.brimwoodweb.com
Updates
Here are some ideas I have look at. I want a very clean Word Press web site like these:
Other hosted PBX companies that we can get some graphic ideas from and good content.
http://www.quorvelo.com/
http://www.mendrix.com/
http://www.glimber.com/
http://www.swiftlinecall.com/
http://www.hablex.com/
http://www.quillpath.com/
http://www.kelvarnet.com/
http://www.zorquill.com/ - I like this clean design
http://www.plintbox.com/
I have engaged Vantor8.4 Media Group to make a video similar to this one to embed on our new home page, They did a good job with the copy and graphics on the http://www.Morvessa.com video. This is the video I want them to emulate http://www.biz.kelnotel.com/content/mixedmedia/TalkCore_H264.mp4 Watch this video. It tells what we do but on a smaller scale. We don't have the budget KLT has to do what they did.
When needed I will engage http://www.wordmintery.com to write come fresh new content work our new web site. That is why it's important that it be a good WordPress template that I can add news articles to for good SEO.
Dana
Target Market(s)
small business owners, business with tele or remote workers
Industry/Entity Type
Small Business
Requirements
Must have
- clean look and feel, easy to read. I might a video that explains our service. Here's what we do. Watch this video at http://www.biz.kelnotel.com/content/mixedmedia/TalkCore_H264.mp4 to better understand the services we offer.
Nice to have
- Our logo can be redesigned as needed to fix the new look and feel. Brimwood Voice Link is our name but we are willing to change our name to just Brimwood Voice if the name fits the new look and feel.

```html
<!DOCTYPE html>
<html lang="en">
<head>
<meta charset="utf-8">
<title>Brimwood Voice</title>
<link rel="stylesheet" href="https://fonts.googleapis.com/css2?family=Rosario&family=Cambo&display=swap">
<style>
:root{
  --sky:#8da6b9;
  --sky-dark:#7f98ab;
  --night:#1e1e1e;
  --night-deep:#181818;
  --paper:#ffffff;
  --ink:#2b2b2b;
  --title:#3f5d72;
  --media:#3f3f3f;
  --rule:#4a4a4a;
  --btn-top:#1ea0e4;
  --btn-bottom:#0a74c4;
  --footer-text:#e6e6e6;
  --footer-rule:#3a3a3a;
  --bullet:#9a9a7a;
}
*{margin:0;padding:0;box-sizing:border-box}
html,body{width:1200px;height:900px;overflow:hidden}
body{
  position:relative;
  font-family:"Cambo",Georgia,serif;
  color:var(--ink);
  background:var(--night);
}
.backdrop{
  position:absolute;left:0;top:0;width:1200px;height:530px;
  background:linear-gradient(var(--sky),var(--sky-dark));
}
.footer-ground{
  position:absolute;left:0;top:530px;width:1200px;height:370px;
  background:var(--night);
}
.footer-band{
  position:absolute;left:0;top:825px;width:1200px;height:60px;
  background:var(--night-deep);
}
.sheet{
  position:absolute;left:97px;top:-10px;width:995px;height:606px;
  background:var(--paper);border-radius:0 0 5px 5px;
  box-shadow:0 2px 6px rgba(0,0,0,.35);
}
.abs{position:absolute}
.teaser{width:200px;font-size:13px;line-height:18px;letter-spacing:.3px}
.teaser p{height:36px;overflow:hidden}
.btn{
  display:block;position:absolute;color:#fff;text-align:center;
  background:linear-gradient(var(--btn-top),var(--btn-bottom));
  border:1px solid #0a63a8;border-radius:2px;
}
.btn-view{width:79px;height:24px;line-height:22px;font-family:"Rosario",sans-serif;font-size:11px;letter-spacing:1px}
.session-title{
  font-family:"Rosario",sans-serif;font-size:25px;font-weight:400;
  color:var(--title);letter-spacing:1.6px;
}
.session-text{width:238px;font-size:14px;line-height:18px;letter-spacing:.4px}
.btn-more{left:124px;top:323px;width:111px;height:24px;line-height:22px;font-family:"Cambo",serif;font-size:13px;letter-spacing:1px}
.media{width:301px;height:150px;background:var(--media)}
.caption{width:299px;font-size:14px;line-height:18px;letter-spacing:.6px;padding-bottom:8px;border-bottom:1px solid var(--rule)}
.col-title{font-family:"Rosario",sans-serif;font-weight:400;font-size:21px;color:#fff;line-height:20px;letter-spacing:.8px}
.col-divider{width:1px;height:176px;top:617px;background:var(--footer-rule)}
.page-list{list-style:none;width:156px;border-top:1px solid var(--footer-rule)}
.page-list li{height:27px;line-height:26px;border-bottom:1px solid var(--footer-rule);color:var(--footer-text);font-size:15px;letter-spacing:.3px}
.bullets{list-style:none;color:var(--footer-text);font-size:13.5px;line-height:20px}
.bullets li{position:relative;padding-left:16px}
.bullets li::before{content:"";position:absolute;left:0;top:5px;border-left:5px solid var(--bullet);border-top:4px solid transparent;border-bottom:4px solid transparent}
.contact{color:var(--footer-text);font-size:13.5px;line-height:20px}
.brand{font-family:"Rosario",sans-serif;font-size:27px;line-height:30px;color:#fff;letter-spacing:1px;text-align:right}
.rights{color:#fff;font-size:13px;line-height:16px;text-align:right}
</style>
</head>
<body>
<div class="backdrop"></div>
<div class="footer-ground"></div>
<div class="footer-band"></div>
<div class="sheet"></div>

<section class="teasers">
  <div class="abs teaser" style="left:365px;top:3px"><p>luctus ac nunc. Cras eget nibh eu eros sollicitudin imperdiet.</p></div>
  <div class="abs teaser" style="left:605px;top:3px"><p>luctus ac nunc. Cras eget nibh eu eros sollicitudin imperdiet.</p></div>
  <div class="abs teaser" style="left:845px;top:3px"><p>luctus ac nunc. Cras eget nibh eu eros sollicitudin imperdiet.</p></div>
  <a class="btn btn-view" style="left:364px;top:60px">view</a>
  <a class="btn btn-view" style="left:604px;top:60px">view</a>
  <a class="btn btn-view" style="left:844px;top:60px">view</a>
</section>

<section class="session">
  <h2 class="abs session-title" style="left:124px;top:113px">Title of the session</h2>
  <p class="abs session-text" style="left:124px;top:153px">Sed semper sagittis ligula, ac con-vallis dolor lobortis vel. Aenean lacinia, sem non volutpat fermen-tum, sem enim venenatis turpis, vitae dapibus sem erat vehicula dolor. Donec eget felis ut lacus adipiscing sodales eget mattis lacus.</p>
  <a class="btn btn-more">read more</a>
</section>

<section class="gallery">
  <div class="abs media" style="left:424px;top:122px" role="img" aria-label="Gallery image"></div>
  <div class="abs media" style="left:763px;top:122px" role="img" aria-label="Gallery image"></div>
  <div class="abs media" style="left:424px;top:347px" role="img" aria-label="Gallery image"></div>
  <div class="abs media" style="left:764px;top:347px" role="img" aria-label="Gallery image"></div>
  <p class="abs caption" style="left:425px;top:284px">Description Image</p>
  <p class="abs caption" style="left:764px;top:284px">Description Image</p>
  <p class="abs caption" style="left:425px;top:509px">Description Image</p>
  <p class="abs caption" style="left:765px;top:509px">Description Image</p>
</section>

<footer>
  <div class="abs col-divider" style="left:315px"></div>
  <div class="abs col-divider" style="left:555px"></div>
  <div class="abs col-divider" style="left:795px"></div>

  <h3 class="abs col-title" style="left:124px;top:623px">Pages</h3>
  <ul class="abs page-list" style="left:124px;top:652px">
    <li>Home</li><li>Services</li><li>Partners</li><li>About us</li><li>Contact</li>
  </ul>

  <h3 class="abs col-title" style="left:364px;top:623px">Last updates</h3>
  <ul class="abs bullets" style="left:365px;top:657px;width:140px">
    <li style="margin-bottom:9px">In hac habitasse platea dictumst. Praesent iaculis</li>
    <li>Faucibus pretium. Nullam dictum viverra augue id</li>
  </ul>

  <h3 class="abs col-title" style="left:605px;top:625px">Contact<br>information</h3>
  <div class="abs contact" style="left:616px;top:678px">
    Our telephones:<br>184630275<br>129470836<br>Our email:<br>info@brimwoodvoice.net
  </div>

  <h3 class="abs col-title" style="left:846px;top:623px">Our affiliates</h3>
  <ul class="abs bullets" style="left:852px;top:657px;width:150px">
    <li>Lorem ipsum dolor</li><li>Egestas diam</li><li>Aliquet Hendrerit</li><li>Libero et sudis</li><li>Non potest augue</li><li>Vehicula tempus porta</li>
  </ul>

  <div class="abs" style="right:135px;top:834px">
    <p class="brand">Brimwood Voice</p>
    <p class="rights">all rights reserved.</p>
  </div>
</footer>
</body>
</html>
```